Professional consulting firm needing a Word document template

I need a Word document template that can be used flexibly for a flyer or brochure of 1 to 3 pages in length. The first page should be designed in a way that it can stand alone as a one-page flyer without a formal cover page. I have attached sample text as a Word document that could be used as the basis for the first 1-2 pages, however I do need three page layouts designed to give flexibility to use as a 3 page booklet. I have attached our brand guidelines, logo, and some stock images that I have previously purchased (they may not all be useful but it gives some options). <br/>The Word document needs to be set up in away that it can easily be edited to accommodate updates to the text, and some variation in the quantity of text on each page. Each page should be able to accommodate a mixture of paragraph text, bullet points, small boxes to call out highlights, one or more images, and some white space to avoid clutter. It should look professional yet engaging and modern.

Font styles to use
Sans Serif

Requirements
Must have
• Must be an editable Microsoft Word document, using the text provided. Must be a layout suitable to use as 1 page, up to 3 pages. Must comply with brand guidelines.

```html
<!DOCTYPE html>
<html lang="en">
<head>
<meta charset="utf-8">
<title>Coreline – Train Driver Competency Indicator Development Project</title>
<link href="https://fonts.googleapis.com/css2?family=Arimo:wght@400;700&display=swap" rel="stylesheet">
<style>
:root{
  --bg:#d9d9d9;
  --navy:#14263a;
  --cyan:#22b6e4;
  --cyan-soft:#7fd3ef;
  --text:#6b6e72;
  --white:#ffffff;
  --photo-a:#1f6f8c;
  --photo-b:#9fe0d4;
}
*{margin:0;padding:0;box-sizing:border-box}
html,body{width:1200px;height:509px;overflow:hidden;background:var(--bg)}
body{position:relative;font-family:'Arimo',Arial,sans-serif;color:var(--text)}
.page{position:absolute;top:27px;width:325px;height:458px;background:var(--white);overflow:hidden;box-shadow:2px 2px 4px rgba(0,0,0,.35)}
.page--one{left:85px}
.page--two{left:440px}
.page--three{left:807px;top:26px}
.abs{position:absolute}
.brand{position:absolute;font-weight:700;letter-spacing:1px;display:flex;align-items:center;gap:5px}
.brand__dot{width:7px;height:7px;border-radius:50%;background:currentColor}
.brand--dark{color:var(--navy);font-size:16px}
.brand--light{color:var(--white);font-size:17px}
.title{position:absolute;color:var(--white);font-weight:700;font-size:9.6px;line-height:11px;text-transform:uppercase}
.lead{position:absolute;color:var(--white);font-size:5.4px;line-height:7.8px}
.copy{position:absolute;font-size:6px;line-height:8.4px;letter-spacing:-.1px}
.copy p+p{margin-top:5px}
.justify{text-align:justify}
.bullets{position:absolute;list-style:none;font-size:6.3px;line-height:11.2px}
.bullets li{position:relative;padding-left:10px}
.bullets li::before{content:"";position:absolute;left:0;top:3px;width:5px;height:5px;border-radius:50%;background:var(--cyan)}
.band{position:absolute;left:0;width:325px;background:var(--cyan);color:var(--white)}
.band__heading{font-weight:700;font-size:8px;text-align:center;margin-top:7px}
.band__body{font-size:6.1px;line-height:8.4px;text-align:center;padding:4px 12px 0}
.footer{position:absolute;left:0;bottom:0;width:325px;height:27px}
.footer a{position:absolute;color:var(--white);font-size:6.4px;text-decoration:underline;top:11px}
.footer .mail{left:39px}
.footer .web{left:225px;top:9px}
.heading-cyan{position:absolute;color:var(--cyan);font-weight:700;font-size:7.5px}
.cell{position:absolute;width:125px}
.cell h3{font-size:5.3px;font-weight:700;text-decoration:underline;color:var(--white);margin-bottom:4px}
.cell p{font-size:4.6px;line-height:5.8px;color:var(--white);text-align:justify}
.cell-icon{position:absolute}
.feature{position:absolute;left:0;width:325px}
.feature p{position:absolute;left:50px;width:260px;font-size:5.7px;line-height:8.4px;color:var(--white)}
</style>
</head>
<body>

<!-- Page one -->
<section class="page page--one">
  <svg class="abs" style="left:0;top:0" width="325" height="170" viewBox="0 0 325 170">
    <rect x="0" y="52" width="325" height="115" fill="var(--navy)"/>
    <polygon points="160,52 325,52 325,57 162,57" fill="var(--cyan-soft)" opacity=".5"/>
    <defs>
      <linearGradient id="tunnel" x1="0" y1="0" x2="1" y2="1">
        <stop offset="0" stop-color="var(--photo-a)"/>
        <stop offset=".55" stop-color="#4fbcc9"/>
        <stop offset="1" stop-color="var(--photo-b)"/>
      </linearGradient>
    </defs>
    <polygon points="182,0 325,0 325,167 212,167" fill="url(#tunnel)" role="img" aria-label="Photo of a train speeding through a lit station with light trails"/>
    <polygon points="180,0 184,0 214,167 210,167" fill="var(--cyan-soft)"/>
  </svg>
  <div class="brand brand--dark" style="left:14px;top:19px"><span class="brand__dot"></span>CORELINE</div>
  <h1 class="title" style="left:14px;top:82px">Train Driver<br>Competency Indicator<br>Development Project</h1>
  <p class="lead" style="left:14px;top:121px;width:170px">We are commencing an applied research project to develop and test a framework of underlying core competencies for train driver performance.</p>

  <p class="copy" style="left:14px;top:180px;width:300px">The objective of the project is to identify observable indicators that describe effective performance in the following types of underlying competencies:</p>
  <ul class="bullets" style="left:23px;top:205px">
    <li>Application of Procedures</li>
    <li>Communication</li>
    <li>Operation of Tools / Equipment</li>
    <li>Problem Solving and Decision Making</li>
    <li>Route Knowledge</li>
    <li>Self Management</li>
  </ul>
  <ul class="bullets" style="left:185px;top:205px">
    <li>Situation Awareness</li>
    <li>System Knowledge</li>
    <li>Teamwork and Leadership</li>
    <li>Train Handling</li>
    <li>Workload Management</li>
  </ul>

  <div class="band" style="top:289px;height:60px">
    <h2 class="band__heading">Underlying competencies:</h2>
    <p class="band__body">The underpinning knowledge and skills required by a train driver, to perform a range of different tasks effectively. Underlying competencies include both ‘technical’ and ‘non-technical’ skills. They are not specific to one driving task, but help build resilient performance across all tasks, conditions or situations that a driver may encounter.</p>
  </div>

  <p class="copy" style="left:14px;top:372px;width:298px">In contrast to other performance marker systems, the current project aims to include both ‘technical’ and ‘non-technical’ skills in an integrated framework, with substantial input from drivers across the industry, both in passenger and freight operations. The aim is to develop a framework that uses a language that describes performance in a way that is relatable to drivers, trainers, and assessors.</p>

  <footer class="footer">
    <svg class="abs" width="325" height="27"><rect width="325" height="27" fill="var(--cyan)"/><polygon points="0,0 163,0 178,27 0,27" fill="var(--navy)"/></svg>
    <a class="mail">contact@corelinegroup.com.au</a>
    <a class="web">www.corelinegroup.com.au</a>
  </footer>
</section>

<!-- Page two -->
<section class="page page--two">
  <svg class="abs" style="left:0;top:0" width="325" height="180" viewBox="0 0 325 180">
    <defs>
      <linearGradient id="yard" x1="0" y1="0" x2="0" y2="1">
        <stop offset="0" stop-color="#3f5872"/>
        <stop offset=".5" stop-color="#6a5a52"/>
        <stop offset="1" stop-color="#c07a3e"/>
      </linearGradient>
    </defs>
    <polygon points="0,0 325,0 325,110 0,177" fill="var(--cyan)"/>
    <polygon points="0,0 325,0 325,102 0,169" fill="var(--navy)"/>
    <polygon points="158,0 325,0 325,102 158,136" fill="url(#yard)" role="img" aria-label="Photo of a rail freight yard at dusk with lit tracks"/>
  </svg>
  <h2 class="abs" style="left:24px;top:24px;color:var(--white);font-size:8.5px;line-height:15px;font-weight:700">What are the benefits for<br>participating organisations?</h2>
  <p class="lead justify" style="left:23px;top:63px;width:124px;font-size:5.3px;line-height:7.7px">All participating rail organisations will receive a copy of the performance indicator framework, which they are free to use or adapt for application within their own operation. A summary report will also be provided, outlining the methodology and aggregated results of the data collection activities. All results will be presented in a de-identified way, to ensure the anonymity of participating organisations and individuals.</p>
  <div class="brand brand--dark" style="left:205px;top:153px">CORELINE<span class="brand__dot"></span></div>

  <h2 class="heading-cyan" style="left:16px;top:188px">What is involved?</h2>
  <p class="copy" style="left:16px;top:200px;width:298px">Participating organisations will be invited to provide in-kind support for the following activities during the period April – June 2020:</p>

  <div class="band" style="top:228px;height:122px">
    <svg class="abs" style="left:0;top:0" width="325" height="122">
      <line x1="162" y1="8" x2="162" y2="118" stroke="var(--white)" stroke-width=".6"/>
      <line x1="16" y1="61" x2="309" y2="61" stroke="var(--white)" stroke-width=".6"/>
    </svg>
    <svg class="cell-icon" style="left:18px;top:9px" width="20" height="16" viewBox="0 0 20 16"><rect x="0" y="0" width="13" height="9" rx="2" fill="var(--navy)"/><polygon points="3,9 6,9 3,12" fill="var(--navy)"/><rect x="7" y="5" width="12" height="8" rx="2" fill="var(--navy)" stroke="var(--cyan)" stroke-width="1"/></svg>
    <div class="cell" style="left:42px;top:8px;width:112px">
      <h3>Interviews with volunteer Driver participants:</h3>
      <p>individual discussions with our researchers about drivers’ previous experiences, to gather information about expert driving strategies and positive techniques used in normal and abnormal operations</p>
    </div>
    <svg class="cell-icon" style="left:175px;top:9px" width="14" height="20" viewBox="0 0 14 20"><rect x="3" y="0" width="8" height="3" fill="var(--navy)"/><circle cx="7" cy="7" r="4" fill="var(--navy)"/><path d="M0 20 Q0 12 7 12 Q14 12 14 20Z" fill="var(--navy)"/></svg>
    <div class="cell" style="left:194px;top:8px;width:118px">
      <h3>Initial workshop:</h3>
      <p>a facilitated group workshop to understand the links between underlying competencies and driving tasks, and to understand Drivers’ perceptions of what each underlying competency looks like in practice.</p>
    </div>
    <svg class="cell-icon" style="left:19px;top:70px" width="14" height="20" viewBox="0 0 14 20"><rect x="0" y="0" width="14" height="15" rx="3" fill="var(--navy)"/><rect x="2" y="3" width="10" height="5" fill="var(--cyan)"/><circle cx="4" cy="11.5" r="1.3" fill="var(--cyan)"/><circle cx="10" cy="11.5" r="1.3" fill="var(--cyan)"/><line x1="3" y1="15" x2="1" y2="20" stroke="var(--navy)" stroke-width="1.4"/><line x1="11" y1="15" x2="13" y2="20" stroke="var(--navy)" stroke-width="1.4"/></svg>
    <div class="cell" style="left:42px;top:66px;width:112px">
      <h3>Driver Training Survey:</h3>
      <p>a voluntary survey will be distributed, requesting Driver Trainers’ and Assessors’ views on the importance of underlying competencies in driving performance, and further data about expert strategies and techniques.</p>
    </div>
    <svg class="cell-icon" style="left:174px;top:66px" width="16" height="16" viewBox="0 0 16 16"><circle cx="8" cy="8" r="7.5" fill="var(--navy)"/><circle cx="5" cy="6" r="1.8" fill="var(--cyan)"/><circle cx="11" cy="6" r="1.8" fill="var(--cyan)"/><circle cx="8" cy="11" r="1.8" fill="var(--cyan)"/></svg>
    <div class="cell" style="left:193px;top:64px;width:119px">
      <h3>Follow-up workshop:</h3>
      <p>a facilitated group workshop to test and refine the performance indicators. Where possible, indicators will be tested through participants providing ratings of a video sample of actual performance, to determine whether multiple raters can distinguish between competency categories.</p>
    </div>
  </div>

  <div class="copy" style="left:16px;top:369px;width:298px">
    <p>It is anticipated that workshops will be run in Brisbane, Sydney and Melbourne. We would appreciate support from participating organisations in providing a workshop venue where possible. Apart from the in-kind support of providing access to personnel and a meeting room, there is no cost associated with participation in the project.</p>
    <p>We look forward to hearing from organisations interested in being part of this landmark project.</p>
  </div>

  <footer class="footer">
    <svg class="abs" width="325" height="27"><rect width="325" height="27" fill="var(--cyan)"/><polygon points="0,0 163,0 178,27 0,27" fill="var(--navy)"/></svg>
    <a class="mail">contact@corelinegroup.com.au</a>
    <a class="web">www.corelinegroup.com.au</a>
  </footer>
</section>

<!-- Page three -->
<section class="page page--three">
  <svg class="abs" style="left:0;top:0" width="325" height="170" viewBox="0 0 325 170">
    <defs>
      <linearGradient id="sunset" x1="0" y1="0" x2="0" y2="1">
        <stop offset="0" stop-color="#3b5a80"/>
        <stop offset=".45" stop-color="#c98a8a"/>
        <stop offset=".7" stop-color="#e9a46a"/>
        <stop offset="1" stop-color="#4a3b3a"/>
      </linearGradient>
    </defs>
    <rect x="0" y="0" width="325" height="168" fill="var(--navy)"/>
    <polygon points="155,0 325,0 325,168 209,168" fill="url(#sunset)" role="img" aria-label="Photo of railway tracks and overhead lines at sunset with a motion-blurred train"/>
  </svg>
  <div class="brand brand--light" style="left:16px;top:42px"><span class="brand__dot"></span>CORELINE</div>
  <h1 class="title" style="left:18px;top:98px">Train Driver<br>Competency Indicator<br>Development Project</h1>

  <p class="copy" style="left:14px;top:183px;width:298px">In contrast to other performance marker systems, the current project aims to include both ‘technical’ and ‘non-technical’ skills in an integrated framework, with substantial input from drivers across the industry, both in passenger and freight operations. The aim is to develop a framework that uses a language that describes performance in a way that is relatable to drivers, trainers, and assessors.</p>

  <div class="band" style="top:231px;height:122px">
    <svg class="abs" style="left:0;top:0" width="50" height="122">
      <g fill="none" stroke="var(--white)" stroke-width=".8">
        <circle cx="25" cy="26" r="11"/>
        <circle cx="25" cy="62" r="11"/>
        <circle cx="25" cy="98" r="11"/>
      </g>
      <g fill="var(--navy)">
        <rect x="19" y="24" width="12" height="4" rx="1"/>
        <circle cx="25" cy="21" r="2.5"/>
        <rect x="21" y="29" width="8" height="3"/>
        <rect x="20" y="56" width="9" height="12" fill="none" stroke="var(--navy)" stroke-width="1"/>
        <line x1="22" y1="60" x2="27" y2="60" stroke="var(--navy)" stroke-width=".8"/>
        <line x1="22" y1="63" x2="27" y2="63" stroke="var(--navy)" stroke-width=".8"/>
        <rect x="24" y="91" width="3" height="7"/>
        <rect x="19" y="98" width="13" height="4" rx="1"/>
      </g>
    </svg>
    <div class="feature" style="top:0">
      <p style="top:21px">Lorem Ipsum. Proin gravida nibh vel velit auctor aliquet. Aenean sollicitudin, lorem quis bibendum auctor Aenean sollicitudin, lorem quis bibendum auctor</p>
      <p style="top:49px">Lorem Ipsum. Proin gravida nibh vel velit auctor aliquet. Aenean sollicitudin, lorem quis bibendum auctor Aenean sollicitudin, lorem quis bibendum auctor Aenean sollicitudin, lorem quis bibendum auctor</p>
      <p style="top:92px">Lorem Ipsum. Proin gravida nibh vel velit auctor aliquet. Aenean sollicitudin, lorem quis bibendum auctor Aenean sollicitudin, lorem quis bibendum auctor</p>
    </div>
  </div>

  <p class="copy justify" style="left:17px;top:369px;width:144px">With substantial input from drivers across the industry, both in passenger and freight operations. The aim is to develop a framework that uses a language that describes performance in a way that is relatable to drivers, trainers, and assessors.</p>
  <p class="copy justify" style="left:170px;top:369px;width:142px">With substantial input from drivers across the industry, both in passenger and freight operations. The aim is to develop a framework that uses a language that describes performance in a way that is relatable to drivers, trainers, and assessors.</p>

  <footer class="footer">
    <svg class="abs" width="325" height="27"><rect width="325" height="27" fill="var(--cyan)"/><polygon points="0,0 163,0 178,27 0,27" fill="var(--navy)"/></svg>
    <a class="mail">contact@corelinegroup.com.au</a>
    <a class="web">www.corelinegroup.com.au</a>
  </footer>
</section>

</body>
</html>
```